Project Willow Crest; Retail packaging for handmade bar soap.

A clean design that conveys quality and affordable luxury. Wrapper material is 80 lb felt cover paper, used as a wrap around the product.

Attached is my idea. Logo is purchased. Unless you think it's terrible, maybe best is to refine what I have? I'm thinking fonts, proportions, etc. Honestly though, if you think it's bad we can start from scratch. I think it's good but I'm not that invested in it. I just want to sell good soap.
5 different fragrances, each identical packaging except the colored stripe and the scent name. Should the scent name be inside the colored stripe or above it?

Apologies for the non-metric:
Soap is 3" tall and 2-13/16" wide and 1" deep.
Front of label is 2-5/16" tall and 2-13/16" wide.
Label (wrap) is 8-1/2" long

Looking forward to hearing from you guys.

Target Market(s)

retail gift shops, health food stores, hotel gift shops.

Industry/Entity Type

retail and online personal care products

Other font styles liked:
• not decorative or script

Colors
0054AA
0677BA
7BADD7
CADEEF
E8F1F8
59FF00
82FF00
B8FF75
E3FFCB
F4FFEA
FFF300
FFF600
FEFA6F
FFFEC7
FFFEE8
EB3D1F
EC4F4E
F09395
F8D3D4
FCEDEE
A7469A
B969AE
D3A5CF
EDDBEB
F8F0F9

Requirements
Must have
• The best word I can think of is feng shui. My soap makes you feel good when you use it. It's simple and clean. I want the same in the label.

```html
<!DOCTYPE html>
<html lang="en">
<head>
<meta charset="utf-8">
<title>Willow Crest Soap Co. – Coconut Lemongrass Wrap</title>
<link rel="stylesheet" href="https://fonts.googleapis.com/css2?family=Bree+Serif&family=Quicksand:wght@400;500&family=Montserrat:wght@400&family=Libre+Baskerville&display=swap">
<style>
  :root {
    --backdrop: #d6d6d2;
    --paper: #ffffff;
    --ink: #1e1e1e;
    --stripe: #f0eb6a;
  }
  html, body {
    margin: 0;
    width: 1200px;
    height: 900px;
    overflow: hidden;
    background: var(--backdrop);
  }
  .wrap-label {
    position: absolute;
    left: 50px;
    top: 300px;
    width: 1100px;
    height: 299px;
    background: var(--paper);
    color: var(--ink);
    box-shadow: 0 3px 8px rgba(0,0,0,0.12);
  }
  .scent-stripe {
    position: absolute;
    left: 0;
    right: 0;
    bottom: 0;
    height: 40px;
    background: var(--stripe);
  }
  .tagline {
    position: absolute;
    left: 98px;
    top: 16px;
    height: 222px;
    writing-mode: vertical-rl;
    transform: rotate(180deg);
    font-family: "Libre Baskerville", serif;
    font-size: 7.5px;
    letter-spacing: 0.22em;
    line-height: 16px;
    text-transform: uppercase;
    text-align: center;
    margin: 0;
  }
  .ingredients {
    position: absolute;
    left: 228px;
    top: 26px;
    width: 290px;
    font-family: "Quicksand", sans-serif;
    font-size: 10px;
    line-height: 14.5px;
    text-align: center;
  }
  .ingredients h2 {
    margin: 0 0 3px;
    font-size: 12px;
    font-weight: 500;
    letter-spacing: 0.04em;
  }
  .ingredients p { margin: 0; }
  .website {
    position: absolute;
    left: 228px;
    top: 195px;
    width: 290px;
    text-align: center;
    font-family: "Quicksand", sans-serif;
    font-weight: 500;
    font-size: 11.5px;
    letter-spacing: 0.03em;
  }
  .net-weight {
    position: absolute;
    top: 230px;
    font-family: "Quicksand", sans-serif;
    font-size: 12px;
    letter-spacing: 0.25em;
  }
  .net-weight.metric { left: 233px; }
  .net-weight.imperial { left: 472px; }
  .origin {
    position: absolute;
    left: 608px;
    top: 60px;
    height: 150px;
    writing-mode: vertical-rl;
    font-family: "Libre Baskerville", serif;
    font-size: 7.5px;
    letter-spacing: 0.25em;
    line-height: 16px;
    text-transform: uppercase;
    text-align: center;
    margin: 0;
  }
  .front-panel {
    position: absolute;
    left: 736px;
    top: 0;
    width: 280px;
    height: 259px;
    text-align: center;
  }
  .brand-name {
    margin: 20px 0 0;
    font-family: "Bree Serif", serif;
    font-weight: 400;
    font-size: 20px;
    letter-spacing: 0.03em;
  }
  .brand-mark {
    display: block;
    margin: 14px auto 0;
  }
  .scent-name {
    position: absolute;
    left: 0;
    right: 0;
    top: 227px;
    margin: 0;
    font-family: "Montserrat", sans-serif;
    font-weight: 400;
    font-size: 15.5px;
    letter-spacing: 0.16em;
    text-transform: uppercase;
  }
</style>
</head>
<body>
  <main class="wrap-label">
    <p class="tagline">This soap's creamy white lather<br>and gentle moisturizers<br>will leave your skin<br>feeling great, every time.</p>

    <section class="ingredients">
      <h2>Ingredients:</h2>
      <p>Soap stuff: vegetable oils (coconut, olive, sustainable certified palm, cocoa, and castor), Oregon Coast artesian spring water, glycerin.</p>
      <p>Goodies: white porcelain clay, Oregon honey, fermentation derived natural citric acid and lactic acid, Oregon sea salt, essential oils and natural fragrances, natural earth oxide colorants. May contain visible coconut shreds or Oregon sea kelp as exfoliant.</p>
    </section>
    <div class="website">WillowCrest.us</div>
    <div class="net-weight metric">130gr</div>
    <div class="net-weight imperial">4.5oz</div>

    <p class="origin">Handmade<br>on the Oregon coast</p>

    <section class="front-panel">
      <h1 class="brand-name">Willow Crest Soap Co.</h1>
      <svg class="brand-mark" width="116" height="142" viewBox="0 0 116 142" role="img" aria-label="Brand illustration: a single-line drawing of a whale">
        <rect width="116" height="142" rx="6" fill="#eeeeec"/>
      </svg>
      <p class="scent-name">Coconut Lemongrass</p>
    </section>

    <div class="scent-stripe"></div>
  </main>
</body>
</html>
```